Tembo & Lusani Advocates website

An interactive professional law firm website fully synchronized with social media pages.

Target Market(s)

Corporations and professionals

Industry/Entity Type

Professional Service

Number of Pages Required

5+ page

Font styles to use
Sans Serif

Colors

Designer to choose colors to be used in the design.

```html
<!DOCTYPE html>
<html lang="en">
<head>
<meta charset="utf-8">
<title>Tembo &amp; Lusani Advocates</title>
<link rel="stylesheet" href="https://fonts.googleapis.com/css2?family=Roboto:wght@400;500&family=Roboto+Condensed:wght@400&family=Open+Sans:wght@400;600&family=Libre+Baskerville:wght@400&display=swap">
<style>
:root{
  --red:#c0272d;
  --nav-red:#a50d10;
  --deep-red:#8f0d12;
  --coral:#f55a5a;
  --navy:#0b1e3a;
  --icon:#a83236;
  --header-bg:#f4f8fc;
  --section-bg:#f8f8f8;
  --text:#2a2a2a;
  --line:#8a8a8a;
}
*{margin:0;padding:0;box-sizing:border-box}
html,body{width:1063px;height:1200px;overflow:hidden;background:var(--section-bg)}
body{position:relative;font-family:"Roboto",sans-serif;color:var(--text)}
.topbar{position:absolute;left:0;top:0;width:1063px;height:33px;background:var(--red);color:#fff;font-family:"Open Sans",sans-serif;font-size:11.5px;letter-spacing:1px}
.topbar .office{position:absolute;left:63px;top:9px}
.topbar .mail{position:absolute;left:625px;top:0;width:216px;height:33px;background:#f06a66;display:flex;align-items:center;gap:8px;padding-left:14px;font-size:11px;letter-spacing:.2px}
.topbar .phone{position:absolute;left:842px;top:0;width:195px;height:33px;background:var(--deep-red);display:flex;align-items:center;gap:12px;padding-left:10px;font-size:12px}
.header{position:absolute;left:0;top:33px;width:1063px;height:157px;background:var(--header-bg)}
.brand{position:absolute;left:0;width:1063px;top:30px;text-align:center;font-family:"Libre Baskerville",serif;font-size:30px;color:#9a1b20;display:flex;justify-content:center;align-items:center;gap:14px}
.brand .mark{width:18px;height:18px;background:#9a1b20}
.tagline{position:absolute;left:0;width:1063px;top:124px;text-align:center;font-family:"Open Sans",sans-serif;font-size:9px;letter-spacing:3.3px;color:#9a1b20}
.nav{position:absolute;left:0;top:190px;width:1063px;height:48px;background:var(--nav-red)}
.nav a{position:absolute;top:0;height:48px;line-height:48px;color:#fff;text-decoration:none;font-size:13px;letter-spacing:-.2px}
.nav .active{left:111px;width:120px;background:var(--navy);text-align:center}
.hero{position:absolute;left:0;top:238px;width:1063px;height:464px;background:linear-gradient(180deg,#1c1a24 0%,#3b2e28 45%,#5b4532 70%,#2a2526 100%)}
.hero h1{position:absolute;left:0;width:1063px;top:158px;text-align:center;font-family:"Libre Baskerville",serif;font-weight:400;font-size:40px;color:#fff;letter-spacing:.5px}
.hero p{position:absolute;left:150px;width:763px;top:233px;text-align:center;font-family:"Open Sans",sans-serif;font-size:15.5px;line-height:24.5px;color:#fff}
.hero .btn{position:absolute;left:432px;top:349px;width:228px;height:38px;background:var(--coral);color:#fff;font-family:"Open Sans",sans-serif;font-weight:600;font-size:15px;line-height:38px;text-align:center}
.practice-title{position:absolute;left:0;width:1063px;top:740px;text-align:center;font-family:"Roboto Condensed",sans-serif;font-size:29px;color:var(--navy)}
.practice-rule{position:absolute;left:507px;top:785px;width:83px;height:2px;background:var(--navy)}
.card{position:absolute;width:203px}
.card .box{height:127px;background:#fff;border:1px solid #ddd;display:flex;align-items:center;justify-content:center}
.card .label{height:43px;display:flex;align-items:center;justify-content:center;text-align:center;font-size:12.5px;font-weight:500;border-bottom:1px solid var(--line);line-height:15px}
.card.row2 .label{height:36px}
.card.featured .label{background:var(--coral);color:#fff;border:none}
.card svg{width:50px;height:50px;fill:none;stroke:var(--icon);stroke-width:2.4;stroke-linecap:round;stroke-linejoin:round}
.cta{position:absolute;left:800px;top:1012px;width:203px;height:170px;background:var(--coral);color:#fff;text-align:center;border:1px solid #e9e9e9}
.cta .head{font-size:15.5px;font-weight:500;margin-top:35px}
.cta .detail{font-size:12.5px;color:#2a1a1a;margin-top:3px}
.cta .head.second{margin-top:26px}
</style>
</head>
<body>
<div class="topbar">
  <span class="office">OFFICES:&nbsp; HARBOURGATE CITY CENTRE</span>
  <span class="mail"><svg width="14" height="11" viewBox="0 0 14 11"><rect x="0" y="0" width="14" height="11" fill="#fff"/><path d="M0 0 L7 6 L14 0" stroke="#f06a66" stroke-width="1.4" fill="none"/></svg>OFFICES@TEMBOLUSANI.CO.UK</span>
  <span class="phone"><svg width="12" height="12" viewBox="0 0 24 24"><path fill="#fff" d="M6.6 10.8a15.1 15.1 0 006.6 6.6l2.2-2.2c.3-.3.7-.4 1-.2 1.1.4 2.3.6 3.6.6.6 0 1 .4 1 1V20c0 .6-.4 1-1 1A17 17 0 013 4c0-.6.4-1 1-1h3.5c.6 0 1 .4 1 1 0 1.3.2 2.5.6 3.6.1.3 0 .7-.2 1z"/></svg>+44 (0)121 555 0148</span>
</div>

<header class="header">
  <div class="brand"><span class="mark"></span>Tembo &amp; Lusani Advocates</div>
  <div class="tagline">CONSTRUCTION LAW &nbsp;| &nbsp;ARBITRATION &nbsp;| &nbsp;LITIGATION</div>
</header>

<nav class="nav">
  <a class="active">HOME</a>
  <a style="left:253px">ABOUT TL LEGAL</a>
  <a style="left:437px">SERVICES »</a>
  <a style="left:577px">NEWS &amp; ARTICLES</a>
  <a style="left:758px">RESOURCES</a>
  <a style="left:904px">CONTACT</a>
</nav>

<section class="hero" role="img" aria-label="Aerial night view of a city centre skyline with lit office towers">
  <h1>LOREM IPSUM DOLOR SIT AMET</h1>
  <p>Aenean imperdiet ante id nisi dapibus sodales. Aenean ex velit, dictum vitae lacus non, accumsan euismod erat. Pellentesque lacinia ex pulvinar, eleifend dui eu, mollis eros. Vivamus sed sagittis neque, vitae bibendum arcu. Duis a velit pretium, sodales justo id, consequat risus. Pellentesque ipsum tellus,</p>
  <div class="btn">Know More</div>
</section>

<h2 class="practice-title">OUR PRACTICE AREA</h2>
<div class="practice-rule"></div>

<div class="card featured" style="left:93px;top:812px">
  <div class="box"><svg viewBox="0 0 50 50"><path d="M6 24 L25 8 L44 24"/><path d="M11 20 V43 H39 V20"/><path d="M18 38 H32"/><path d="M20 29 L27 22"/><rect x="24" y="17" width="6" height="9" transform="rotate(45 27 21.5)"/></svg></div>
  <div class="label">DISPUTE RESOLUTION &amp;<br>LITIGATION</div>
</div>
<div class="card" style="left:329px;top:812px">
  <div class="box"><svg viewBox="0 0 50 50"><rect x="22" y="6" width="10" height="18" transform="rotate(45 27 15)"/><path d="M22 22 L7 38"/><path d="M24 38 H44 V44 H24 Z"/><path d="M28 33 H40"/></svg></div>
  <div class="label">EMPLOYMENT</div>
</div>
<div class="card" style="left:564px;top:812px">
  <div class="box"><svg viewBox="0 0 50 50"><circle cx="16" cy="9" r="4"/><circle cx="33" cy="9" r="4"/><path d="M10 44 V28 L12 18 H20 L22 28 V44"/><path d="M16 30 V44"/><path d="M27 44 V28 L29 18 H37 L39 28 V44"/><path d="M33 30 V44"/></svg></div>
  <div class="label">COMERCIAL</div>
</div>
<div class="card" style="left:800px;top:812px">
  <div class="box"><svg viewBox="0 0 50 50"><path d="M4 5 L12 13 M12 5 L4 13"/><circle cx="43" cy="15" r="3" fill="#a83236"/><circle cx="9" cy="40" r="3" fill="#a83236"/><path d="M27 35 L35 43 M35 35 L27 43"/><path d="M12 31 C14 20 22 14 32 15"/><path d="M27 11 L32 15 L27 19"/></svg></div>
  <div class="label">FINANCIAL SERVICES</div>
</div>

<div class="card row2" style="left:93px;top:1019px">
  <div class="box"><svg viewBox="0 0 50 50"><rect x="22" y="6" width="10" height="18" transform="rotate(45 27 15)"/><path d="M22 22 L7 38"/><path d="M24 38 H44 V44 H24 Z"/><path d="M28 33 H40"/></svg></div>
  <div class="label">INSOLVENCY</div>
</div>
<div class="card row2" style="left:329px;top:1019px">
  <div class="box"><svg viewBox="0 0 50 50"><circle cx="16" cy="9" r="4"/><circle cx="33" cy="9" r="4"/><path d="M10 44 V28 L12 18 H20 L22 28 V44"/><path d="M16 30 V44"/><path d="M27 44 V28 L29 18 H37 L39 28 V44"/><path d="M33 30 V44"/></svg></div>
  <div class="label">DIRECTOR DISQUALIFICATION</div>
</div>
<div class="card row2" style="left:564px;top:1019px">
  <div class="box"><svg viewBox="0 0 50 50"><path d="M4 5 L12 13 M12 5 L4 13"/><circle cx="43" cy="15" r="3" fill="#a83236"/><circle cx="9" cy="40" r="3" fill="#a83236"/><path d="M27 35 L35 43 M35 35 L27 43"/><path d="M12 31 C14 20 22 14 32 15"/><path d="M27 11 L32 15 L27 19"/></svg></div>
  <div class="label">INHERITANCE DISPUTE</div>
</div>

<aside class="cta">
  <div class="head">CALL US TODAY</div>
  <div class="detail">(704) 555-0192</div>
  <div class="head second">EMAIL US NOW</div>
  <div class="detail">office@tembolusani.co.uk</div>
</aside>
</body>
</html>
```